Business Card Design

Selling beds and mattrices
See website www.lumirest.com.au for details
Targeting wholesale bed sellers

Industry/Entity Type

Business

Contact Information for Business Card

Lumirest
Director Gerald Pinwick
Beds and Mattrices - Most technologically advanced beds in the world
European designed and made
Already No 1 seller in Europe
Call now for a quote
ph: 0472 918 305
Email: sales@lumirest.com.au
www.lumirest.com.au

```html
<!DOCTYPE html>
<html lang="en">
<head>
<meta charset="utf-8">
<title>Lumirest Business Card</title>
<link href="https://fonts.googleapis.com/css2?family=Lato:wght@400;700&display=swap" rel="stylesheet">
<style>
  :root {
    --page-bg: #e9e6e1;
    --card-bg: #ffffff;
    --ink: #111111;
    --ink-soft: #5e5e5e;
    --label-grey: #8c8c8c;
    --band: #0d0d0d;
    --tab: #8e8e8e;
    --photo-light: #e4e4e4;
    --photo-dark: #2e2e2e;
  }
  * { box-sizing: border-box; margin: 0; padding: 0; }
  html, body { width: 1200px; height: 1000px; overflow: hidden; }
  body {
    background: var(--page-bg);
    font-family: "Lato", Arial, sans-serif;
    color: var(--ink);
    position: relative;
  }
  .card {
    position: absolute;
    left: 215px;
    width: 770px;
    height: 440px;
    background: var(--card-bg);
    box-shadow: 0 6px 18px rgba(0,0,0,0.18);
    overflow: hidden;
  }
  .card--front { top: 40px; }
  .card--back { top: 520px; }

  .brand {
    position: absolute;
    left: 0; right: 0;
    text-align: center;
  }
  .brand__name {
    display: inline-flex;
    align-items: center;
    gap: 14px;
    font-size: 52px;
    font-weight: 400;
    letter-spacing: 3px;
    color: var(--ink);
    text-transform: uppercase;
  }
  .brand__mark {
    width: 16px; height: 16px;
    background: var(--ink);
  }
  .brand__region {
    display: block;
    font-size: 12px;
    letter-spacing: 1px;
    margin-top: 4px;
    padding-left: 300px;
    color: var(--ink);
  }
  .card--front .brand { top: 34px; }
  .card--back .brand { top: 40px; }

  .tagline {
    position: absolute;
    top: 150px;
    left: 0; right: 0;
    text-align: center;
    font-size: 19px;
    line-height: 1.25;
    color: var(--ink-soft);
  }
  .product-photo {
    position: absolute;
    left: 0; right: 0; bottom: 0;
    height: 215px;
    background: linear-gradient(180deg, var(--photo-light) 0%, #cfcfcf 45%, var(--photo-dark) 100%);
  }

  .contact {
    position: absolute;
    top: 165px;
    left: 0; right: 0;
    text-align: center;
  }
  .contact__name {
    font-size: 23px;
    font-weight: 700;
    letter-spacing: 1.5px;
    text-transform: uppercase;
  }
  .contact__role {
    font-size: 16px;
    color: var(--label-grey);
    margin-top: 2px;
  }
  .contact__list {
    list-style: none;
    margin-top: 38px;
    font-size: 19px;
    line-height: 1.35;
  }
  .contact__label {
    color: var(--label-grey);
    font-weight: 700;
  }
  .footer-band {
    position: absolute;
    left: 0; right: 0; bottom: 0;
    height: 30px;
    background: var(--band);
  }
  .company-number {
    position: absolute;
    bottom: 14px;
    left: 50%;
    transform: translateX(-50%);
    width: 272px;
    height: 34px;
    line-height: 34px;
    text-align: center;
    background: var(--tab);
    border-radius: 3px;
    font-size: 18px;
    color: var(--ink);
    letter-spacing: 0.5px;
  }
</style>
</head>
<body>
  <section class="card card--front">
    <div class="brand">
      <span class="brand__name"><span class="brand__mark"></span>Lumirest</span>
      <span class="brand__region">AUSTRALIA</span>
    </div>
    <p class="tagline">Beds and Mattrices - Most Technologically Advanced Beds in the World<br>European Designed and Made Already No 1 Seller in Europe.</p>
    <div class="product-photo" role="img" aria-label="Photo of a dark upholstered bed with white mattress in a bright room with framed art and a vase"></div>
  </section>

  <section class="card card--back">
    <div class="brand">
      <span class="brand__name"><span class="brand__mark"></span>Lumirest</span>
      <span class="brand__region">AUSTRALIA</span>
    </div>
    <div class="contact">
      <h1 class="contact__name">Gerald Pinwick</h1>
      <p class="contact__role">Director</p>
      <ul class="contact__list">
        <li><span class="contact__label">Phone:</span> 0472 918 305 (For a Quote)</li>
        <li><span class="contact__label">Email:</span> sales@lumirest.com.au</li>
        <li><span class="contact__label">Website:</span> www.lumirest.com.au</li>
      </ul>
    </div>
    <div class="footer-band"></div>
    <div class="company-number">ACN 284 519 736</div>
  </section>
</body>
</html>
```